Luxury Brand Real Estate For Sale sign

**Update** I've added some examples from the internet of other signs that have a look similar to what I would like to see. I do not want my personal name in the sign. And the word FOR SALE Does not need to be so large - it can be more subtle.
I want to create a Real Estate for sale sign for my company that will be used for luxury/higher end real estate listings. I’m sharing my business card as well as a logo with new teal color to show what we're moving towards: we’re using Teal, white, black and gold.
Hoping the sign is simple, sophisticated and eye catching.
The sign should be 24" wide by 30" tall including the company name: Harbor Crest Realty Group and our logo, office phone number 727-555-0148 and website www.hcrgexample.com the words "For Sale"
Optional to add this e-mail address info@hcrgexample.com to the sign
Target Market(s)
Luxury home buyers
Industry/Entity Type
Real Estate
Look and feel

```html
<!DOCTYPE html>
<html lang="en">
<head>
<meta charset="utf-8">
<title>Harbor Crest Realty Group — For Sale Sign</title>
<link rel="stylesheet" href="https://fonts.googleapis.com/css2?family=Montserrat:wght@300;400&family=Oswald:wght@200;300&display=swap">
<style>
  :root {
    --paper: #ffffff;
    --teal: #10837f;
    --band: #000000;
    --gold: #c4a024;
    --ink: #111111;
    --white: #ffffff;
  }
  html, body {
    margin: 0;
    padding: 0;
    width: 962px;
    height: 1200px;
    overflow: hidden;
    background: var(--paper);
  }
  .sign {
    display: block;
    width: 962px;
    height: 1200px;
  }
  .sign__panel { fill: var(--teal); }
  .sign__band { fill: var(--band); }
  .brand__mark { fill: none; stroke: var(--ink); stroke-width: 3; }
  .brand__divider { stroke: var(--ink); stroke-width: 3; }
  .brand__name {
    font-family: "Montserrat", sans-serif;
    font-weight: 400;
    fill: var(--ink);
  }
  .headline {
    font-family: "Oswald", sans-serif;
    font-weight: 300;
    fill: var(--gold);
  }
  .phone {
    font-family: "Oswald", sans-serif;
    font-weight: 200;
    fill: var(--white);
  }
  .website {
    font-family: "Montserrat", sans-serif;
    font-weight: 300;
    fill: var(--white);
  }
</style>
</head>
<body>
<svg class="sign" viewBox="0 0 962 1200" xmlns="http://www.w3.org/2000/svg" role="img" aria-label="Harbor Crest Realty Group For Sale sign">
  <rect class="sign__panel" x="17" y="21" width="928" height="1159" rx="39" ry="39"/>
  <rect class="sign__band" x="17" y="326" width="928" height="484"/>

  <g class="brand">
    <rect class="brand__mark" x="144" y="129" width="181" height="92"/>
    <line class="brand__divider" x1="358" y1="88" x2="358" y2="267"/>
    <text class="brand__name" x="395" y="173" font-size="38" textLength="447" lengthAdjust="spacingAndGlyphs">HARBOR CREST</text>
    <text class="brand__name" x="395" y="207" font-size="20" letter-spacing="12">REALTY GROUP</text>
  </g>

  <text class="headline" x="490" y="566" font-size="226" text-anchor="middle" textLength="656" lengthAdjust="spacingAndGlyphs">FOR SALE</text>
  <text class="phone" x="481" y="733" font-size="158" text-anchor="middle" textLength="671" lengthAdjust="spacingAndGlyphs">727-555-0148</text>

  <text class="website" x="481" y="1032" font-size="96" text-anchor="middle" textLength="720" lengthAdjust="spacingAndGlyphs">www.hcrgexample.com</text>
</svg>
</body>
</html>
```